Event flyer for Sunday night Youth Group

Need a 4 x 6 or 5 x 7 flyer for a new youth group starting on April 14. The youth group is for students in middle school and high school so it needs to look fun and cool, but not childish. I prefer it not to include pictures of people unless it's so obscure you can't really see their faces. I've uploaded some pictures of flyers I like. I've also attached a couple versions of our logo to use on the flyer.
Information the flyer needs to include:
Youth Group
Sundays, 6-8pm (beginning April 14)
Location: Merriwick's - 4219 Hollowfern Ln S, Ashbury, 97418
There will be dinner, games, friends, and a message.
Target Market(s)
Youth ages 13-18
Industry/Entity Type
Church
Colors
Designer to choose colors to be used in the design.
Look and feel

```html
<!DOCTYPE html>
<html lang="en">
<head>
<meta charset="utf-8">
<title>Youth Group Flyer</title>
<link href="https://fonts.googleapis.com/css2?family=Arvo:wght@700&family=Montserrat:wght@400;500;600;700&family=Poppins:wght@400;600&family=Great+Vibes&display=swap" rel="stylesheet">
<style>
  :root{
    --stage:#161818;
    --flyer:#1d2b2e;
    --shape-dark:#172326;
    --shape-mid:#24464b;
    --frame:#2f5a5e;
    --disc:#2e4a52;
    --yellow:#e3dc3a;
    --white:#f1f3f2;
    --soft:#d5dcdb;
    --pill:#8f9d95;
    --pill-text:#26302f;
  }
  *{margin:0;padding:0;box-sizing:border-box}
  html,body{width:1200px;height:797px;overflow:hidden;background:var(--stage)}
  .flyer{position:absolute;left:330px;top:18px;width:540px;height:760px;background:var(--flyer);overflow:hidden}
  .backdrop{position:absolute;inset:0}
  .brand{position:absolute;top:38px;left:0;right:0;display:flex;justify-content:center;align-items:center;gap:14px}
  .brand-dot{width:34px;height:34px;border-radius:50%;background:var(--white)}
  .brand-rule{width:1px;height:46px;background:var(--white)}
  .brand-name{font-family:"Montserrat",sans-serif;font-weight:500;color:var(--white);letter-spacing:2px;line-height:1.15;font-size:20px}
  .brand-name span{display:block;font-size:13px;letter-spacing:5px;padding-left:22px}
  .emblem{position:absolute;left:0;top:0}
  .venue{position:absolute;top:500px;left:0;right:0;text-align:center}
  .pin{display:block;margin:0 auto 6px}
  .address{display:inline-block;background:var(--pill);color:var(--pill-text);font-family:"Poppins",sans-serif;font-weight:600;font-size:14px;padding:5px 18px;border-radius:5px}
  .lineup-title{position:absolute;top:580px;left:0;right:0;text-align:center;font-family:"Great Vibes",cursive;color:var(--yellow);font-size:28px}
  .lineup{position:absolute;top:622px;left:40px;right:40px;display:flex;justify-content:space-between}
  .item{width:104px;text-align:center;position:relative}
  .item + .item::before{content:"";position:absolute;left:-10px;top:6px;height:90px;border-left:1px dashed rgba(241,243,242,.35)}
  .photo{width:84px;height:84px;border-radius:50%;margin:0 auto;border:2px solid var(--soft)}
  .photo.dinner{background:radial-gradient(circle at 40% 40%,#b98a5c,#5a3a24 75%)}
  .photo.games{background:radial-gradient(circle at 50% 60%,#e07a2e,#6b2c14 75%)}
  .photo.friends{background:linear-gradient(160deg,#d8e2ea,#7b94ad 70%)}
  .photo.message{background:linear-gradient(200deg,#3b5d8a,#c9ccd0 80%)}
  .label{margin-top:8px;font-family:"Poppins",sans-serif;font-size:15px;color:var(--white)}
</style>
</head>
<body>
<main class="flyer">
  <svg class="backdrop" width="540" height="760" viewBox="0 0 540 760" aria-hidden="true">
    <polygon points="0,0 540,0 540,260 300,0" fill="var(--shape-dark)"/>
    <polygon points="0,420 0,760 330,760" fill="var(--shape-mid)" opacity=".55"/>
    <polygon points="540,470 540,760 250,760" fill="var(--shape-dark)"/>
    <polygon points="0,0 140,0 0,180" fill="var(--shape-mid)" opacity=".5"/>
    <rect x="18" y="18" width="504" height="724" fill="none" stroke="var(--frame)" stroke-width="3"/>
  </svg>

  <header class="brand">
    <div class="brand-dot"></div>
    <div class="brand-rule"></div>
    <div class="brand-name">LANTERNWAY<span>FELLOWSHIP</span></div>
  </header>

  <svg class="emblem" width="540" height="500" viewBox="0 0 540 500">
    <defs>
      <path id="arc-title" d="M110,330 A160,160 0 0 1 430,330"/>
      <path id="arc-time" d="M120,300 A150,150 0 0 0 420,300"/>
    </defs>
    <circle cx="270" cy="300" r="186" fill="var(--disc)"/>
    <circle cx="270" cy="300" r="174" fill="none" stroke="var(--yellow)" stroke-width="2" stroke-dasharray="1 5" stroke-linecap="round"/>
    <text font-family="Arvo, serif" font-weight="700" font-size="76" fill="var(--yellow)">
      <textPath href="#arc-title" startOffset="50%" text-anchor="middle">YOUTH</textPath>
    </text>
    <text x="270" y="258" text-anchor="middle" font-family="Montserrat, sans-serif" font-weight="500" font-size="34" fill="var(--soft)">GROUP</text>
    <text x="270" y="296" text-anchor="middle" font-family="Great Vibes, cursive" font-size="30" fill="var(--white)">beginning</text>
    <line x1="160" y1="310" x2="380" y2="310" stroke="var(--yellow)" stroke-width="1"/>
    <text x="270" y="358" text-anchor="middle" font-family="Montserrat, sans-serif" font-weight="700" font-size="46" fill="var(--soft)">14<tspan font-size="24" dy="-16" dx="8">TH</tspan><tspan dy="16" dx="10">APRIL</tspan></text>
    <circle cx="270" cy="392" r="13" fill="var(--white)"/>
    <text font-family="Montserrat, sans-serif" font-weight="500" font-size="21" fill="var(--white)" letter-spacing="2">
      <textPath href="#arc-time" startOffset="50%" text-anchor="middle">SUNDAY 6PM TO 8PM</textPath>
    </text>
  </svg>

  <section class="venue">
    <svg class="pin" width="22" height="26" viewBox="0 0 22 26" aria-hidden="true">
      <path d="M11 1C5.5 1 1.5 5 1.5 10.2 1.5 17 11 25 11 25s9.5-8 9.5-14.8C20.5 5 16.5 1 11 1z" fill="var(--white)"/>
      <circle cx="11" cy="10" r="3.6" fill="var(--flyer)"/>
    </svg>
    <p class="address">Merriwick's - 4219 Hollowfern Ln S, Ashbury, 97418</p>
  </section>

  <p class="lineup-title">There will be</p>
  <section class="lineup">
    <div class="item"><div class="photo dinner" role="img" aria-label="Photo of a shared dinner table"></div><p class="label">Dinner</p></div>
    <div class="item"><div class="photo games" role="img" aria-label="Photo of games by a warm fire"></div><p class="label">Games</p></div>
    <div class="item"><div class="photo friends" role="img" aria-label="Photo of friends together, seen from behind"></div><p class="label">Friends</p></div>
    <div class="item"><div class="photo message" role="img" aria-label="Photo of an open book for the message"></div><p class="label">A Message</p></div>
  </section>
</main>
</body>
</html>
```